We need a single web page design for a promotion. This page will acts as a landing page for users. Please provide us with a cutting edge design. I have attached a previous design used a couple of years ago.

Link: http://www.brightkettlestudio.example/freegift/

The Start Here box needs to look like this:

-Start Here (heading) 
-A box for email addresses to be entered
-Then a check box with "Yes, I have read and agree to the Privacy Policy and agree to receive email marketing from Bright Kettle Studio and acknowledge that I will receive special email offers from our marketing partners, including the Harbor Ledger newsletter."
-A submit button 

All of this information needs to be in one box please.  And please feel free to contact me if you have any questions about this. 

Target Market(s)

Middle aged women (housewives)

Requirements
Must have
• Images must reflect the "500 Photo Prints". The only fields that are necessary are a box for email and a submit button.
Should not have
• The word FREE anywhere on the page

```html
<!DOCTYPE html>
<html lang="en">
<head>
<meta charset="utf-8">
<title>500 Photo Prints Delivered To You</title>
<link rel="stylesheet" href="https://fonts.googleapis.com/css2?family=Montserrat:wght@400;700&family=Questrial&family=Arimo:wght@400;700&display=swap">
<style>
  :root {
    --page-blue: #3c5a8d;
    --header-blue: #304f84;
    --header-edge: #28446f;
    --footer-navy: #213656;
    --panel-bg: #e8edf4;
    --panel-dots: #5b78a6;
    --ink-navy: #1f3357;
    --ink-body: #44526a;
    --button-navy: #1c2f52;
    --field-border: #9aa9bf;
    --white: #ffffff;
    --soft-white: #dfe6f1;
    --photo-edge: #f4f4f4;
    --card-back: #c9ccd2;
    --card-accent: #b56a3c;
  }
  * { box-sizing: border-box; margin: 0; padding: 0; }
  html, body { width: 1200px; height: 920px; overflow: hidden; }
  body {
    position: relative;
    background: var(--page-blue);
    font-family: "Arimo", Arial, sans-serif;
    color: var(--white);
  }

  .promo-header {
    position: absolute; left: 0; top: 0;
    width: 1200px; height: 131px;
    background: linear-gradient(var(--header-blue), var(--header-edge));
    box-shadow: 0 3px 8px rgba(0,0,0,0.3);
    display: flex; align-items: center; justify-content: center;
  }
  .promo-title {
    font-family: "Questrial", "Montserrat", sans-serif;
    font-weight: 400; font-size: 50px; letter-spacing: 0;
    color: var(--white); margin-top: -8px;
  }
  .promo-title strong { font-family: "Montserrat", sans-serif; font-weight: 700; font-size: 47px; }

  .signup-panel {
    position: absolute; left: 71px; top: 296px;
    width: 469px; height: 252px;
    background: var(--panel-bg);
    box-shadow: 0 6px 10px rgba(0,0,0,0.35);
    padding: 9px;
  }
  .signup-inner {
    position: relative; width: 100%; height: 100%;
    border: 1px dashed var(--panel-dots);
  }
  .camera-art {
    position: absolute; left: 14px; top: 24px;
    width: 132px; height: 128px;
    background: linear-gradient(160deg, #6f9bd3 0%, #4a6e9c 45%, #cfd3d8 70%, #8f959c 100%);
    border: 4px solid var(--white);
    transform: rotate(-4deg);
    box-shadow: 1px 2px 5px rgba(0,0,0,0.35);
  }
  .start-heading {
    position: absolute; right: 20px; top: 16px;
    font-family: "Questrial", sans-serif; font-weight: 400;
    font-size: 27px; color: var(--ink-navy); letter-spacing: 0.5px;
  }
  .start-rule {
    position: absolute; left: 168px; right: 12px; top: 56px;
    border-top: 1px solid #c2ccdb;
  }
  .email-field {
    position: absolute; left: 168px; top: 64px;
    width: 266px; height: 28px;
    border: 1px solid var(--field-border);
    background: var(--white);
    font-family: "Arimo", sans-serif; font-size: 13px;
    color: #7c7c7c; padding: 0 10px;
  }
  .email-field::placeholder { color: #7c7c7c; }
  .consent-row {
    position: absolute; left: 168px; top: 101px;
    width: 266px;
    display: flex; gap: 6px; align-items: flex-start;
    font-size: 10.5px; line-height: 13px; color: var(--ink-body);
  }
  .consent-box {
    flex: 0 0 auto; width: 12px; height: 12px; margin-top: 1px;
    accent-color: var(--button-navy);
  }
  .submit-button {
    position: absolute; left: 354px; top: 191px;
    width: 80px; height: 29px;
    background: var(--button-navy); border: none;
    font-family: "Arimo", sans-serif; font-weight: 700;
    font-size: 12px; color: var(--white); letter-spacing: 0.3px;
  }

  .feature-line {
    position: absolute; left: 71px; top: 566px;
    font-size: 13px; color: var(--soft-white);
  }
  .feature-line .sep { margin: 0 8px; }

  .photo-stack {
    position: absolute; left: 748px;
    width: 388px; height: 184px;
  }
  .photo-stack .card-back {
    position: absolute; inset: 6px 4px 4px 6px;
    background: var(--card-back);
    border: 6px solid var(--photo-edge);
    transform: rotate(-2.5deg);
    box-shadow: 2px 3px 6px rgba(0,0,0,0.35);
  }
  .photo-stack .card-mid {
    position: absolute; inset: 4px 10px 6px 2px;
    background: var(--card-accent);
    border: 6px solid var(--photo-edge);
    transform: rotate(1.8deg);
    box-shadow: 2px 3px 6px rgba(0,0,0,0.3);
  }
  .photo-stack .photo-front {
    position: absolute; inset: 10px 8px 10px 8px;
    border: 7px solid var(--photo-edge);
    box-shadow: 3px 5px 8px rgba(0,0,0,0.4);
  }
  .stack-one   { top: 169px; }
  .stack-two   { top: 376px; }
  .stack-three { top: 584px; }
  .stack-one .photo-front   { background: linear-gradient(100deg, #3d2a1d 0%, #7b5a3e 40%, #d9c3ad 60%, #5a4130 100%); }
  .stack-two .photo-front   { background: linear-gradient(110deg, #d7a55a 0%, #b97c4c 35%, #e8d7b0 60%, #8fae5d 100%); }
  .stack-three .photo-front { background: linear-gradient(160deg, #3b8fd8 0%, #7fbaf0 40%, #e4b393 70%, #d46b52 100%); }

  .offer-note {
    position: absolute; left: 0; top: 829px; width: 1200px;
    text-align: center; font-size: 13px; color: var(--soft-white);
    letter-spacing: 0.2px;
  }

  .page-footer {
    position: absolute; left: 0; top: 862px;
    width: 1200px; height: 58px;
    background: var(--footer-navy);
    display: flex; align-items: center; justify-content: center;
    font-size: 13px; color: #b8c3d6;
  }
  .page-footer .sep { margin: 0 7px; }
</style>
</head>
<body>
  <header class="promo-header">
    <h1 class="promo-title">Get 500 Photo Prints <strong>DELIVERED TO YOU</strong></h1>
  </header>

  <form class="signup-panel" action="http://www.brightkettlestudio.example/freegift/">
    <div class="signup-inner">
      <div class="camera-art" role="img" aria-label="Digital camera with a landscape print"></div>
      <h2 class="start-heading">START HERE</h2>
      <div class="start-rule"></div>
      <input class="email-field" type="email" placeholder="Enter Email here">
      <label class="consent-row">
        <input class="consent-box" type="checkbox">
        <span>Yes, I have read and agree to the Privacy Policy and agree to receive email marketing from Bright Kettle Studio and acknowledge that I will receive special email offers from our marketing partners, including the Harbor Ledger newsletter.</span>
      </label>
      <button class="submit-button" type="submit">SUBMIT</button>
    </div>
  </form>

  <p class="feature-line">Professional Quality Photos<span class="sep">|</span>Unlimited storage<span class="sep">|</span>Share with Family &amp; Friends</p>

  <div class="photo-stack stack-one">
    <div class="card-back"></div><div class="card-mid"></div>
    <div class="photo-front" role="img" aria-label="Printed portrait photo of a bride"></div>
  </div>
  <div class="photo-stack stack-two">
    <div class="card-back"></div><div class="card-mid"></div>
    <div class="photo-front" role="img" aria-label="Printed photo of a family outdoors"></div>
  </div>
  <div class="photo-stack stack-three">
    <div class="card-back"></div><div class="card-mid"></div>
    <div class="photo-front" role="img" aria-label="Printed photo of friends under a blue sky"></div>
  </div>

  <p class="offer-note">*OFFER REDEMPTION WILL REQUIRE PARTICIPATION AND / OR PURCHASE OF THIRD PARTY OFFERS</p>

  <footer class="page-footer">
    Copyright © 2011 All rights reserved. Privacy Policy<span class="sep">|</span>Unsubscribe
  </footer>
</body>
</html>
```